Gale Sentry - WEBSITE Contest - 4-5 pages coding - Strong, simple clean WORDPRESS

Hello,
The inspiriation website is www.brixhalo.com
Please look at this site because I want to copy that.
I have changed the order a little bit so please look at my order of the site elements.
I will supply text, please just use lorem ipsum for now.
PLEASE LOOK AT THE BRIX HALO WEBSITE AND MAKE A COPY OF THAT.
PPlease look at that site and see the different features it has and make that.
We will need this main page and then:
-About Us page
-Contact Us page
-Request a quote page / fillable form
-1 product/service page
Thank you,
Trevor
/////////////////////////////
Website design for Gale Sentry.
Please design with simple, easy to read fonts. Customers are older and need strong, bold easy to read.
galesentry-demo.com
Tel (555) 318-4072
trevor@galesentry-demo.com
The problem is that all roofing vents leak. We have a product that goes into the vent that stops the roof from leaking.
Your beautiful Florida home is unprotected!
All roof vents leak!
Winds over 30 MPH push rainwater INTO your home through the rooftop vents! The result is water damage that can cost thousands of dollars to repair and remediate!
The GALE SENTRY is a powerful roof vent protection system, engineered to block wind driven rains from entering your home's roof vents.
The Gale Sentry is made to withstand extreme conditions. Featuring IMPACT hurricane screening and powerful steel construction.
Professional installation is permanent and concealed and is accomplished via the roof top.
Get protected for all the storms ahead! Get the Gale Sentry!
www.galesentry-demo.com
Call Now: 555 318-4072
Updates
Hello to all designers - please add a "SERVICE AREA MAP" widget to the designs. Thank you.
Target Market(s)
The target customer is a affluent, older couple 50-60 years old. Homeowner. middle class to upper class adults / ages 50-60 years old (older but not VERY old)
Industry/Entity Type
roofing and construction
Coding
Coded - Design and coding required
Number of Pages Required
4 page
Colors
Designer to choose colors to be used in the design.
Requirements
Must have
- Great landing page, about us page, product page, contact us page, request quote form / Strong, simple clean
Nice to have
- feelings: professional / strong / reliable / safety / shelter / security / future stability/ calm / security
Should not have
- stress / fear feeling - this product will remove fear and stress of damages from storms

```html
<!DOCTYPE html>
<html lang="en">
<head>
<meta charset="utf-8">
<title>Gale Sentry – Roof Vent Protection</title>
<link href="https://fonts.googleapis.com/css2?family=Montserrat:wght@400;500;600;700;800&display=swap" rel="stylesheet">
<style>
:root{
  --brand:#0d5596;
  --brand-dark:#0b4a85;
  --bar:#0e5491;
  --accent:#1e93e6;
  --ink:#1c1f24;
  --body:#4a4f57;
  --muted:#8a9099;
  --pale:#f3f5f8;
  --white:#ffffff;
  --footer:#141517;
}
*{box-sizing:border-box;margin:0;padding:0}
html,body{width:1200px;height:3346px;overflow:hidden}
body{font-family:'Montserrat',sans-serif;color:var(--body);background:var(--white);position:relative}
.abs{position:absolute}
a{color:inherit;text-decoration:none}

/* top bar */
.topbar{left:0;top:0;width:1200px;height:33px;background:var(--brand-dark)}
.topbar .contact-strip{left:701px;top:0;width:499px;height:33px;background:var(--bar)}
.social-mini{top:6px;width:20px;height:20px;border:1px solid rgba(255,255,255,.7);border-radius:50%}
.top-item{font-size:12px;color:var(--white);display:flex;align-items:center;gap:8px}
.top-icon{width:18px;height:18px;background:#29a8e8;border-radius:3px;display:flex;align-items:center;justify-content:center}

/* nav */
.nav{left:0;top:33px;width:1200px;height:75px;background:var(--white)}
.brand{display:flex;align-items:center;gap:10px}
.brand-dot{width:44px;height:44px;border-radius:50%;background:var(--brand)}
.brand-name{font-weight:600;font-size:21px;color:var(--brand);letter-spacing:.5px}
.menu a{position:absolute;top:28px;font-size:12px;font-weight:500;color:var(--ink);letter-spacing:.3px}
.menu a.active{color:var(--accent)}
.menu a.active::after{content:"";position:absolute;left:0;right:0;bottom:-5px;height:2px;background:var(--accent)}

/* hero */
.hero{left:0;top:108px;width:1200px;height:492px;
  background:
    radial-gradient(ellipse 420px 300px at 900px 230px,rgba(38,52,34,.85),rgba(38,52,34,0) 70%),
    radial-gradient(ellipse 300px 140px at 200px 470px,rgba(30,44,28,.9),rgba(30,44,28,0) 75%),
    radial-gradient(ellipse 380px 120px at 620px 480px,rgba(40,52,34,.8),rgba(40,52,34,0) 75%),
    linear-gradient(180deg,#5f6264 0%,#858789 30%,#9a9c9c 55%,#7c807c 80%,#4d554a 100%)}
.hero-over{left:0;top:0;width:1200px;height:492px;background:linear-gradient(90deg,rgba(25,28,32,.35),rgba(25,28,32,0) 55%)}
.hero .kicker{left:130px;top:146px;font-size:20px;font-weight:600;color:var(--white);letter-spacing:.5px}
.hero h1{left:128px;top:170px;font-size:45px;line-height:56px;font-weight:800;color:var(--white)}
.hero p{left:130px;top:300px;width:470px;font-size:12.5px;line-height:20px;color:var(--white)}
.btn{display:flex;align-items:center;justify-content:center;gap:8px;background:var(--brand);color:var(--white);font-size:11px;font-weight:700;letter-spacing:.4px}
.btn .ring{width:7px;height:7px;border:2px solid var(--white);border-radius:50%}

/* section text */
.label{font-size:14.5px;font-weight:500;color:var(--brand);letter-spacing:.5px}
.h2{font-size:33px;line-height:43px;font-weight:500;color:var(--ink)}
.para{font-size:12.5px;line-height:19.5px;color:var(--body)}

/* about */
.about-art{left:130px;top:675px;width:400px;height:400px;border-radius:50%;
  background:
    radial-gradient(circle at 48% 48%,#3ab3b8 0%,#2e9bad 18%,#2a7fa8 34%,rgba(42,127,168,0) 46%),
    radial-gradient(circle at 70% 85%,rgba(150,175,200,.55),rgba(150,175,200,0) 40%),
    radial-gradient(circle at 25% 25%,#3a6f9c,#2b5d8e 50%,#1f4d7b 100%)}

/* featured */
.featured{left:0;top:1140px;width:1200px;height:439px;overflow:hidden;
  background:
    radial-gradient(ellipse 260px 220px at 500px 120px,rgba(120,110,96,.45),rgba(120,110,96,0) 70%),
    radial-gradient(ellipse 420px 160px at 380px 420px,rgba(20,22,26,.9),rgba(20,22,26,0) 75%),
    linear-gradient(90deg,#26282a 0%,#3a3936 38%,#2d2e30 60%,#1d2126 100%)}
.featured .label,.featured .h2,.featured .para{color:var(--white)}
.product-photo{left:695px;top:33px;width:376px;height:376px;border-radius:50%;
  background:
    radial-gradient(ellipse 200px 90px at 300px 70px,rgba(70,92,60,.95),rgba(70,92,60,0) 70%),
    radial-gradient(ellipse 160px 120px at 60px 70px,rgba(168,176,176,.9),rgba(168,176,176,0) 75%),
    radial-gradient(ellipse 140px 90px at 340px 330px,rgba(40,44,46,.95),rgba(40,44,46,0) 75%),
    linear-gradient(165deg,#8c918c 0%,#c9cdca 32%,#b5b9b6 50%,#8f9390 68%,#6a6f6d 100%)}

/* video */
.video-sec{left:0;top:1579px;width:1200px;height:457px;background:var(--pale)}
.video{left:591px;top:77px;width:479px;height:302px;
  background:
    radial-gradient(ellipse 300px 60px at 240px 250px,rgba(140,80,70,.45),rgba(140,80,70,0) 75%),
    radial-gradient(ellipse 360px 90px at 260px 170px,rgba(44,58,46,.85),rgba(44,58,46,0) 75%),
    linear-gradient(180deg,#7a8080 0%,#6b7170 40%,#4b5550 65%,#3a423d 100%)}
.play{left:217px;top:129px;width:46px;height:46px;border:2px solid rgba(255,255,255,.85);border-radius:50%}

/* contact */
.contact{left:0;top:2036px;width:1200px;height:438px;overflow:hidden;
  background:
    radial-gradient(ellipse 260px 200px at 260px 360px,rgba(90,60,40,.6),rgba(90,60,40,0) 75%),
    radial-gradient(ellipse 260px 160px at 1080px 300px,rgba(70,62,50,.55),rgba(70,62,50,0) 75%),
    linear-gradient(100deg,#3a4654 0%,#262b31 38%,#1d2228 62%,#2b2e2a 100%)}
.contact .label,.contact .h2{color:var(--white)}
.field{font-size:10.5px;color:var(--white)}
.field-line{height:1px;background:rgba(255,255,255,.75)}
.submit{left:549px;top:335px;width:108px;height:35px;background:var(--white);color:var(--ink);font-size:11px;font-weight:500;display:flex;align-items:center;justify-content:center;letter-spacing:.4px}

/* testimonials */
.testi{left:0;top:2474px;width:1200px;height:472px;background:linear-gradient(180deg,#f2f5f8,#eef2f6)}
.card{width:439px;height:244px;background:var(--white);border-left:6px solid var(--accent);box-shadow:0 8px 30px rgba(20,40,70,.07)}
.avatar{left:31px;top:34px;width:72px;height:72px;border-radius:50%;background:linear-gradient(135deg,#c9b29a,#8e7a66);box-shadow:4px 0 0 var(--accent)}
.person{left:125px;top:58px}
.person strong{display:block;font-size:16.5px;font-weight:500;color:var(--ink)}
.person span{font-size:9.5px;color:var(--muted)}
.ribbon{left:369px;top:105px;width:85px;height:34px}
.quote{left:28px;top:149px;width:380px;font-size:12px;line-height:18px;color:var(--body)}

/* footer */
.footer{left:0;top:2946px;width:1200px;height:400px;background:var(--footer);color:#cfd2d6}
.footer h4{font-size:17.5px;font-weight:500;color:var(--white)}
.f-links a{display:block;font-size:12px;line-height:29px;color:#c6c9cd}
.f-contact{font-size:12px;line-height:17px;color:#c6c9cd;display:flex;gap:12px}
.f-icon{width:20px;height:24px;background:var(--brand);flex:none;display:flex;align-items:center;justify-content:center}
.f-social{width:32px;height:32px;border-radius:50%;background:#222428}
</style>
</head>
<body>

<div class="abs topbar">
  <div class="abs contact-strip"></div>
  <span class="abs social-mini" style="left:130px" aria-label="Social link"></span>
  <span class="abs social-mini" style="left:158px" aria-label="Social link"></span>
  <span class="abs social-mini" style="left:187px" aria-label="Social link"></span>
  <div class="abs top-item" style="left:737px;top:7px">
    <span class="top-icon"><svg width="10" height="10" viewBox="0 0 24 24"><path fill="#fff" d="M6.6 10.8a15 15 0 0 0 6.6 6.6l2.2-2.2c.3-.3.7-.4 1-.2 1.1.4 2.3.6 3.6.6.6 0 1 .4 1 1V20c0 .6-.4 1-1 1A17 17 0 0 1 3 4c0-.6.4-1 1-1h3.5c.6 0 1 .4 1 1 0 1.3.2 2.5.6 3.6.1.3 0 .7-.2 1z"/></svg></span>(555) 318-4072
  </div>
  <div class="abs top-item" style="left:872px;top:7px">
    <span class="top-icon"><svg width="11" height="9" viewBox="0 0 24 18"><rect x="1" y="1" width="22" height="16" fill="none" stroke="#fff" stroke-width="2"/><path d="M1 1l11 9 11-9" fill="none" stroke="#fff" stroke-width="2"/></svg></span>trevor@galesentry-demo.com
  </div>
</div>

<header class="abs nav">
  <div class="abs brand" style="left:130px;top:15px">
    <span class="brand-dot"></span><span class="brand-name">GALE SENTRY</span>
  </div>
  <nav class="menu">
    <a class="active" style="left:686px">HOME</a>
    <a style="left:772px">ABOUT US</a>
    <a style="left:885px">PRODUCT</a>
    <a style="left:994px">CONTACT US</a>
  </nav>
</header>

<section class="abs hero" role="img" aria-label="Palm trees bending in storm winds under a grey sky">
  <div class="abs hero-over"></div>
  <div class="abs kicker">YOUR BEAUTIFUL</div>
  <h1 class="abs">FLORIDA HOME IS<br>UNPROTECTED!</h1>
  <p class="abs">Are you already a current Squall Shield customer and need to order replacement T4 fasteners for your window frames?</p>
  <a class="abs btn" style="left:130px;top:365px;width:125px;height:36px"><span class="ring"></span>GET STARTED</a>
</section>

<section>
  <div class="abs about-art" role="img" aria-label="Circular photo of palm trees against a stormy blue sky"></div>
  <div class="abs label" style="left:610px;top:737px">ABOUT US</div>
  <h2 class="abs h2" style="left:610px;top:758px">Welcome To Gale<br>Sentry</h2>
  <p class="abs para" style="left:609px;top:866px;width:455px">But I must explain to you how all this mistaken idea of denouncing pleasure and praising pain was born and I will give you a complete account of the system, and expound the actual teachings of the great explorer of the truth, the master-builder of human happiness.</p>
  <a class="abs btn" style="left:609px;top:975px;width:126px;height:37px"><span class="ring"></span>READ MORE</a>
</section>

<section class="abs featured" role="img" aria-label="Worker in a hard hat installing metal roofing">
  <svg class="abs" style="left:0;top:0" width="1200" height="439" viewBox="0 0 1200 439">
    <polygon points="900,0 1200,0 1200,260 1060,300" fill="#12579a"/>
    <polygon points="700,0 820,0 1000,230 920,300" fill="#2a2c30" opacity=".75"/>
    <line x1="852" y1="0" x2="872" y2="26" stroke="#1e93e6" stroke-width="5"/>
    <line x1="888" y1="0" x2="910" y2="26" stroke="#1e93e6" stroke-width="5"/>
    <line x1="1058" y1="290" x2="1146" y2="439" stroke="#1e93e6" stroke-width="5"/>
  </svg>
  <div class="abs product-photo" role="img" aria-label="Steel roof vent guard with round vent holes resting on grass"></div>
  <div class="abs label" style="left:130px;top:101px">FEATURED PRODUCTS</div>
  <h2 class="abs h2" style="left:130px;top:122px">Gale Sentry</h2>
  <p class="abs para" style="left:129px;top:190px;width:410px">But I must explain to you how all this mistaken idea of denouncing pleasure and praising pain was born and I will give you a complete account of the system, and expound the actual teachings of the great explorer of the truth, the master-builder of human happiness.</p>
  <a class="abs btn" style="left:130px;top:299px;width:126px;height:38px"><span class="ring"></span>VIEW DETAILS</a>
</section>

<section class="abs video-sec">
  <div class="abs label" style="left:130px;top:140px">DIY HURRICANE PROTECTION.</div>
  <h2 class="abs h2" style="left:130px;top:161px">Squall Shield Testing<br>Videos</h2>
  <p class="abs para" style="left:129px;top:265px;width:415px">But I must explain to you how all this mistaken idea of denouncing pleasure and praising pain was born and I will give you a complete account of the system, and expound the actual teachings of the great explorer of the truth, the master-builder of human happiness.</p>
  <div class="abs video" role="img" aria-label="Video still of palm trees in hurricane winds over rooftops">
    <div class="abs play"></div>
    <svg class="abs" style="left:236px;top:146px" width="12" height="14" viewBox="0 0 12 14"><path d="M1 0l11 7-11 7z" fill="#fff"/></svg>
  </div>
</section>

<section class="abs contact" role="img" aria-label="Dark metal roof on a house at dusk">
  <svg class="abs" style="left:0;top:0" width="1200" height="438" viewBox="0 0 1200 438">
    <polygon points="0,0 340,0 0,400" fill="#0d5596" opacity=".85"/>
    <line x1="370" y1="0" x2="112" y2="438" stroke="#1e93e6" stroke-width="5"/>
    <line x1="402" y1="0" x2="220" y2="312" stroke="#1e93e6" stroke-width="5"/>
  </svg>
  <div class="abs label" style="left:549px;top:46px">CONTACT</div>
  <h2 class="abs h2" style="left:549px;top:63px;font-size:32px">Get In Touch</h2>
  <div class="abs field" style="left:549px;top:114px">Sed ut perspiciatis unde omnis iste natus error sit voluptatem</div>
  <div class="abs field" style="left:551px;top:176px">First Name:</div>
  <div class="abs field-line" style="left:549px;top:193px;width:254px"></div>
  <div class="abs field" style="left:816px;top:176px">Last Name:</div>
  <div class="abs field-line" style="left:816px;top:193px;width:254px"></div>
  <div class="abs field" style="left:551px;top:218px">Email:</div>
  <div class="abs field-line" style="left:549px;top:235px;width:254px"></div>
  <div class="abs field" style="left:816px;top:218px">Phone:</div>
  <div class="abs field-line" style="left:816px;top:235px;width:254px"></div>
  <div class="abs field" style="left:551px;top:251px">Message:</div>
  <div class="abs field-line" style="left:549px;top:317px;width:521px"></div>
  <a class="abs submit">SUBMIT</a>
</section>

<section class="abs testi">
  <div class="abs label" style="left:0;top:63px;width:1200px;text-align:center">TESTIMONIAL</div>
  <h2 class="abs h2" style="left:0;top:88px;width:1200px;text-align:center">What they’re Ttalking About us</h2>

  <article class="abs card" style="left:130px;top:161px">
    <div class="abs avatar" role="img" aria-label="Portrait photo of client"></div>
    <div class="abs person"><strong>Daniel Hale</strong><span>Business Consultant</span></div>
    <svg class="abs ribbon" viewBox="0 0 85 34"><rect width="85" height="24" fill="#0d5596"/><polygon points="64,24 85,24 85,34" fill="#0a3f70"/><text x="9" y="16" fill="#fff" font-size="11" font-family="Montserrat,sans-serif">★ ★ ★ ★ ★</text></svg>
    <p class="abs quote">Sed ut perspiciatis unde omnis iste natus error sit voluptatem accusantium doloremque laudantium, totam rem aperiam, eaque ipsa quae ab illo inventore veritatis et quasi architecto beatae vitae dicta sunt explicabo.</p>
  </article>

  <article class="abs card" style="left:609px;top:161px">
    <div class="abs avatar" role="img" aria-label="Portrait photo of client" style="background:linear-gradient(135deg,#e2c6a2,#b08a62)"></div>
    <div class="abs person"><strong>Daniel Hale</strong><span>Business Consultant</span></div>
    <svg class="abs ribbon" viewBox="0 0 85 34"><rect width="85" height="24" fill="#0d5596"/><polygon points="64,24 85,24 85,34" fill="#0a3f70"/><text x="9" y="16" fill="#fff" font-size="11" font-family="Montserrat,sans-serif">★ ★ ★ ★ ★</text></svg>
    <p class="abs quote">Sed ut perspiciatis unde omnis iste natus error sit voluptatem accusantium doloremque laudantium, totam rem aperiam, eaque ipsa quae ab illo inventore veritatis et quasi architecto beatae vitae dicta sunt explicabo.</p>
  </article>
</section>

<footer class="abs footer">
  <div class="abs brand" style="left:130px;top:99px">
    <span class="brand-dot" style="background:var(--white);width:46px;height:46px"></span>
    <span class="brand-name" style="color:var(--white);font-size:26px">GALE SENTRY</span>
  </div>
  <p class="abs" style="left:130px;top:178px;width:310px;font-size:12px;line-height:19.5px;color:#c6c9cd">Sed ut perspiciatis unde omnis iste natus error sit voluptatem accusantium doloremque laudantium, totam rem aperiam</p>

  <h4 class="abs" style="left:509px;top:72px">Quick Links</h4>
  <div class="abs f-links" style="left:509px;top:109px">
    <a>Home</a><a>About Us</a><a>Products</a><a>Contact Us</a>
  </div>

  <h4 class="abs" style="left:683px;top:72px">Contact Us</h4>
  <div class="abs f-contact" style="left:683px;top:116px">
    <span class="f-icon"><svg width="10" height="12" viewBox="0 0 24 28"><path fill="#fff" d="M12 0a9 9 0 0 0-9 9c0 7 9 19 9 19s9-12 9-19a9 9 0 0 0-9-9zm0 12a3 3 0 1 1 0-6 3 3 0 0 1 0 6z"/></svg></span>
    <span>42/K Lorem ipsum dolar sit amet<br>Florida 25KL00 USA</span>
  </div>
  <div class="abs f-contact" style="left:683px;top:186px;align-items:center">
    <span class="f-icon"><svg width="10" height="10" viewBox="0 0 24 24"><path fill="#fff" d="M6.6 10.8a15 15 0 0 0 6.6 6.6l2.2-2.2c.3-.3.7-.4 1-.2 1.1.4 2.3.6 3.6.6.6 0 1 .4 1 1V20c0 .6-.4 1-1 1A17 17 0 0 1 3 4c0-.6.4-1 1-1h3.5c.6 0 1 .4 1 1 0 1.3.2 2.5.6 3.6.1.3 0 .7-.2 1z"/></svg></span>
    <span>(555) 318-4072</span>
  </div>
  <div class="abs f-contact" style="left:683px;top:240px;align-items:center">
    <span class="f-icon"><svg width="11" height="9" viewBox="0 0 24 18"><rect x="1" y="1" width="22" height="16" fill="none" stroke="#fff" stroke-width="2"/><path d="M1 1l11 9 11-9" fill="none" stroke="#fff" stroke-width="2"/></svg></span>
    <span>trevor@galesentry-demo.com</span>
  </div>

  <h4 class="abs" style="left:962px;top:72px">Others</h4>
  <div class="abs f-links" style="left:962px;top:109px">
    <a>Cookies Policy</a><a>Privacy Policy</a><a>Terms &amp; Condition</a><a>Help!</a>
  </div>

  <span class="abs f-social" style="left:131px;top:290px" aria-label="Social link"></span>
  <span class="abs f-social" style="left:172px;top:290px" aria-label="Social link"></span>
  <span class="abs f-social" style="left:214px;top:290px" aria-label="Social link"></span>
  <div class="abs" style="left:265px;top:306px;width:540px;height:1px;background:#26282c"></div>
  <div class="abs" style="left:700px;top:300px;width:370px;text-align:right;font-size:9.5px;color:#6f747b">Copyright © 2016 <span style="color:#fff">Gale Sentry</span>. All rights reserved.</div>
</footer>

</body>
</html>
```